Brindle cards

I am in the auto motive, transportation business I would like a business card that is Something cool, modern edgy, having to do with car culture. I offer towing service for high and exotic cars. I also provide towing for collisions and car accidents. I offer open and enclosed transport nationwide.

Target Market(s)

Car culture people high end auto collectors

Industry/Entity Type

Towing car carrier

Contact Information for Business Card

My company colors black yellow and silver

Font styles to use
Serif

```html
<!DOCTYPE html>
<html lang="en">
<head>
<meta charset="utf-8">
<title>Brindle Transportation – Business Cards</title>
<link href="https://fonts.googleapis.com/css2?family=Arimo:wght@400;700&display=swap" rel="stylesheet">
<style>
  :root {
    --page-bg: #2b2b2b;
    --card-black: #1e1e1e;
    --card-deep: #121212;
    --brand-yellow: #f2dc3c;
    --brand-silver: #c4c4c4;
    --text-white: #f4f4f4;
  }
  * { box-sizing: border-box; margin: 0; padding: 0; }
  html, body {
    width: 1200px; height: 900px; overflow: hidden;
    background: var(--page-bg);
    font-family: "Arimo", Arial, sans-serif;
  }
  .canvas { position: relative; width: 1200px; height: 900px; }
  .card {
    position: absolute; left: 320px; width: 560px; height: 320px;
    background: var(--card-black);
    border-left: 4px solid var(--brand-yellow);
    border-bottom: 4px solid var(--brand-yellow);
    box-shadow: 0 14px 30px rgba(0,0,0,.55);
    overflow: hidden;
  }
  .card-back { top: 100px; background: var(--card-deep); }
  .card-front { top: 470px; }

  .back-pattern {
    position: absolute; inset: 0;
    background: linear-gradient(135deg, #0e0e0e 0%, #1a1a1a 55%, #262626 100%);
  }
  .back-wordmark {
    position: absolute; right: 60px; top: 110px;
    display: flex; align-items: center; gap: 10px;
    color: var(--brand-yellow);
    font-weight: 700; font-size: 30px; letter-spacing: 1px; text-transform: uppercase;
  }
  .mark-dot { width: 14px; height: 14px; border-radius: 50%; background: var(--brand-yellow); }

  .front-wordmark {
    position: absolute; left: 24px; top: 60px; width: 250px; height: 200px;
    display: flex; flex-direction: column; justify-content: center; align-items: center;
    color: var(--brand-silver);
    font-weight: 700; font-size: 22px; line-height: 1.2;
    text-transform: uppercase; text-align: center; white-space: nowrap;
  }
  .divider {
    position: absolute; left: 290px; top: 60px; width: 2px; height: 200px;
    background: var(--brand-yellow);
  }
  .contact-block {
    position: absolute; left: 312px; top: 62px; color: var(--text-white);
    font-size: 13px; line-height: 1.35;
  }
  .person-name {
    color: var(--brand-yellow); font-weight: 700; font-size: 19px; letter-spacing: .5px;
    text-transform: uppercase;
  }
  .person-title { margin-bottom: 10px; }
  .address { margin-bottom: 12px; }
  .contact-list { list-style: none; }
  .contact-list li { display: flex; align-items: center; gap: 8px; margin-bottom: 3px; }
  .contact-list svg { width: 13px; height: 13px; flex: none; }
</style>
</head>
<body>
<main class="canvas">

  <section class="card card-back">
    <div class="back-pattern" role="img" aria-label="Faint repeating brand pattern in gloss black on matte black"></div>
    <div class="back-wordmark"><span class="mark-dot"></span>Brindle</div>
  </section>

  <section class="card card-front">
    <div class="front-wordmark"><span>Brindle</span><span>Transportation</span></div>
    <div class="divider"></div>
    <div class="contact-block">
      <p class="person-name">Dana Whitlock</p>
      <p class="person-title">CEO/Founder</p>
      <p class="address">P.O. Box 3178 Harbor Road<br>Country Name AB 6210</p>
      <ul class="contact-list">
        <li>
          <svg viewBox="0 0 16 16" aria-hidden="true"><path fill="#f2dc3c" d="M3 1l3 3-2 2c1 2 3 4 5 5l2-2 3 3-2 2C7 14 2 9 1 3z"/></svg>
          (555) 318 4402
        </li>
        <li>
          <svg viewBox="0 0 16 16" aria-hidden="true"><rect x="4" y="1" width="8" height="14" rx="1.5" fill="none" stroke="#f2dc3c" stroke-width="1.6"/><circle cx="8" cy="12.5" r="1" fill="#f2dc3c"/></svg>
          (555) 742 9016
        </li>
        <li>
          <svg viewBox="0 0 16 16" aria-hidden="true"><rect x="1" y="3" width="14" height="10" fill="#f2dc3c"/><path d="M1 3l7 6 7-6" fill="none" stroke="#1e1e1e" stroke-width="1.4"/></svg>
          info@brindletransportation.com
        </li>
        <li>
          <svg viewBox="0 0 16 16" aria-hidden="true"><g fill="none" stroke="#f2dc3c" stroke-width="1.3"><circle cx="8" cy="8" r="6.5"/><ellipse cx="8" cy="8" rx="3" ry="6.5"/><path d="M1.5 8h13M2.5 5h11M2.5 11h11"/></g></svg>
          www.brindletransportation.com
        </li>
      </ul>
    </div>
  </section>

</main>
</body>
</html>
```